Marlow Crest Group (Real Estate and Investment)

A high end, clean design.
We are a real estate company with sales, asset management and investment divisions. We want to use a black and white scheme which is really high end feel. The back of the card can just be the logo (black background with the white writing) as we will probably emboss this when we print)

Target Market(s)

High level investors, high end houses for sale

Industry/Entity Type

Business

Contact Information for Business Card

Name, position, phone number and email address
Glen Varley, Managing Director, 0437259064 and glen@marlowcrest-example.com.au

Requirements
Must have
• Back of the card to be the black background with the white writing (as per the attached images). Would like the capacity to emboss the writing and logo

```html
<!DOCTYPE html>
<html lang="en">
<head>
<meta charset="utf-8">
<title>Marlow Crest Group – Business Card</title>
<link rel="stylesheet" href="https://fonts.googleapis.com/css2?family=Montserrat:wght@400;600&display=swap">
<style>
  :root {
    --backdrop: #2a2826;
    --card: #0e0e0e;
    --card-edge: #1c1c1c;
    --white: #f4f4f4;
    --muted: #9a9a9a;
    --emboss: #3a3a3a;
  }
  * { margin: 0; padding: 0; box-sizing: border-box; }
  html, body {
    width: 1200px;
    height: 716px;
    overflow: hidden;
    background: var(--backdrop);
    font-family: "Montserrat", sans-serif;
  }
  .stage {
    position: relative;
    width: 1200px;
    height: 716px;
    display: flex;
    align-items: center;
    justify-content: center;
    gap: 60px;
  }
  .card {
    position: relative;
    width: 500px;
    height: 286px;
    background: var(--card);
    border: 1px solid var(--card-edge);
    box-shadow: 0 18px 40px rgba(0,0,0,0.55);
  }
  .card-back {
    display: flex;
    align-items: center;
    justify-content: center;
  }
  .brand-name {
    font-weight: 600;
    text-transform: uppercase;
    letter-spacing: 0.04em;
  }
  .card-back .brand-name {
    font-size: 30px;
    color: var(--emboss);
  }
  .card-front .brand-name {
    position: absolute;
    left: 40px;
    top: 58px;
    font-size: 24px;
    color: var(--white);
  }
  .brand-mark {
    position: absolute;
    left: 40px;
    top: 24px;
    width: 22px;
    height: 22px;
    border: 1.5px solid var(--white);
    border-radius: 50%;
  }
  .person {
    position: absolute;
    left: 40px;
    top: 122px;
    width: 220px;
    border-bottom: 1.5px solid var(--white);
    padding-bottom: 8px;
  }
  .person-name {
    font-size: 13px;
    font-weight: 600;
    color: var(--white);
  }
  .person-role {
    font-size: 9px;
    color: var(--muted);
    margin-top: 2px;
  }
  .contact-list {
    position: absolute;
    left: 40px;
    top: 186px;
    list-style: none;
  }
  .contact-item {
    display: flex;
    align-items: center;
    gap: 10px;
    font-size: 11px;
    color: var(--white);
    margin-bottom: 9px;
  }
  .contact-icon { width: 12px; height: 12px; flex: none; }
</style>
</head>
<body>
  <main class="stage">
    <section class="card card-back" aria-label="Card back">
      <p class="brand-name">Marlow Crest Group</p>
    </section>

    <section class="card card-front" aria-label="Card front">
      <span class="brand-mark" aria-hidden="true"></span>
      <p class="brand-name">Marlow Crest Group</p>

      <div class="person">
        <p class="person-name">Glen Varley</p>
        <p class="person-role">Managing Director</p>
      </div>

      <ul class="contact-list">
        <li class="contact-item">
          <svg class="contact-icon" viewBox="0 0 24 24" aria-hidden="true">
            <path fill="#f4f4f4" d="M6.6 10.8c1.4 2.8 3.8 5.1 6.6 6.6l2.2-2.2c.3-.3.7-.4 1-.2 1.1.4 2.3.6 3.6.6.6 0 1 .4 1 1V20c0 .6-.4 1-1 1C10.6 21 3 13.4 3 4c0-.6.4-1 1-1h3.5c.6 0 1 .4 1 1 0 1.2.2 2.4.6 3.6.1.3 0 .7-.2 1z"/>
          </svg>
          <span>0437259064</span>
        </li>
        <li class="contact-item">
          <svg class="contact-icon" viewBox="0 0 24 24" aria-hidden="true">
            <rect x="2.5" y="5" width="19" height="14" fill="none" stroke="#f4f4f4" stroke-width="2"/>
            <path d="M3 6l9 7 9-7" fill="none" stroke="#f4f4f4" stroke-width="2"/>
          </svg>
          <span>glen@marlowcrest-example.com.au</span>
        </li>
      </ul>
    </section>
  </main>
</body>
</html>
```